Domestic Violence Consulting Firm needs double sided page flyer

We need a flyer for an upcoming Juvenile Justice conference in Florida that addresses a form of domestic violence called child to parent violence or parent abuse. This is when an adolescent is aggressive, abusive and violent toward a parent or caregiver and is arrested for Domestic Violence. The child attends Mending Roots Family Program with their parent who is the victim. We would like to see traditional DV photos but a with a new twist of the parent being the victim. The final design should promote shock to this new subject of domestic violence and interest to our program that addresses this subject. You can get more information about this at www.hearthwardsupport.example
Updates

REVISED CONTENT WITH A CALL TO ACTION Who we are: The silent suffering of parents abused by their adolescent is a serious and often hidden issue within families. Adolescent to Parent Abuse, internationally known as Child to Parent Violence is a complex family and public health problem. Stories from parents who are willing to speak about their abuse reveal the pain of victims who must by law care for their abuser. Abuse by teens in the home feels extremely violating as a youth steps out of their place in the natural family hierarchy. Understandably so, parents are often exhausted, carry deep grief as victims, feel shock and become isolated in shame and blame with nowhere to turn for understanding or help. Parents are not alone in their frustration and confusion associated with how to address Child to Parent Violence. Juvenile Justice Judges, State District Attorneys, Probation Officers, Child Welfare Case Managers and Law Enforcement Officers are often frustrated by who to turn to for professional services to intervene in this silent epidemic. Therefore, Mending Roots Consulting offers an array of consultative, collaborative and experienced professional services to a variety of clientele affected by Child to Parent Violence. Our specialized approach takes into account the serious ongoing need for safety of each family member. We have extensive experience with the nuances of this particular family and community challenge and offer a haven of safety to address this highly stigmatized topic. What we do: Mending Roots Family Program (bold) is conducted in a unique group setting within the juvenile justice probation and diversion program where families significantly reduce abuse and violence within the home. Parents and youth work together with trained facilitators through ten highly relational, psycho-educational sessions. Youth face their behaviors with weekly accountability and without minimizing, justifying or denying their disrespectful and abusive acts. Mending Roots Family Coaching (bold) is a private option for parents that encourages exploration of each family's values and individuality and facilitates discovery of their own personalized parenting style that respects the uniqueness of each family member and acknowledges the special history of each family unit. Mending Roots Training (bold) offers customized live and e-learning seminars, presentations, webinars and continued educational trainings for organizations. We are nationally recognized trainers in Adult and Youth Emotional Steady Aid and Balanced Living Renewal Map (BLRM). Train the trainer course for the Mending Roots Family Program is available upon request. Why we are the experts: We recognize that the relationship between a parent-child has a distinctiveness unlike those of intimate partners and requires a different approach. We address the societal concerns and needs of public safety, by providing youth with necessary and supportive accountability for their abuse behaviors through our Mending Roots Family Program. We honor each family’s culture, acknowledges the trauma of parenting a teen with abusive behaviors, nurtures each family’s strengths, and empowers all families to identify their individual needs. We motivate individuals, families and community with a focus on the global and basic human need for safety. We, the program designers, are recognized as subject matter experts on the topic and present at numerous local, state and national venues. We offer private consultative, collaborative and experienced professional services to agencies, communities and parents. Contact us today: facebook, website, twitter, linkedin (Call to action)

REVISED CONTENT FOR DOUBLE SIDED FLYER The silent suffering of parents abused by their adolescent is a serious and often hidden issue within families. Adolescent to Parent Abuse, internationally known as Child to Parent Violence is a complex family and public health problem. Stories from parents who are willing to speak about their abuse reveal the pain of victims who must by law care for their abuser. Abuse by teens in the home feels extremely violating as a youth steps out of their place in the natural family hierarchy and behaves with a squad of disrespectful and intense behaviors. Understandably so, parents are often exhausted, carry deep grief as victims, feel shock at experiencing their child’s abuse, and become isolated in shame and blame with nowhere to turn for understanding or help. Parents are not alone in their frustration and confusion associated with how to address Child to Parent Violence. Juvenile Justice Judges, State District Attorneys, Probation Officers, Child Welfare Case Managers and Law Enforcement Officers are often frustrated by who to turn to for professional services to intervene in this silent epidemic. Therefore, Mending Roots Consulting (bold) offers an array of consultative, collaborative and experienced professional services to a variety of clientele affected by Child to Parent Violence. Our specialized approach takes into account the serious ongoing need for safety of each family member. We have extensive experience with the nuances of this particular family and community challenge and offer a haven of safety to address this highly stigmatized topic. What we offer: Mending Roots Family Program (bold) is conducted in a unique group setting within the juvenile justice probation and diversion program where families significantly reduce abuse and violence within the home. Parents and youth work together with trained facilitators through ten highly relational, psycho-educational sessions. Youth face their behaviors with weekly accountability and without minimizing, justifying or denying their disrespectful and abusive acts. Mending Roots Family Coaching (bold) is a private option for parents that encourages exploration of each family's values and individuality and facilitates discovery of their own personalized parenting style that respects the uniqueness of each family member and acknowledges the special history of each family unit. Mending Roots Training (bold) offers customized live and e-learning seminars, webinars and continued educational trainings for organizations. We are nationally recognized trainers in Adult and Youth Emotional Steady Aid and Balanced Living Renewal Map (BLRM). Train the trainer course for the Mending Roots Family Program is available. How we are different: We recognize that the relationship between a parent-child has a distinctiveness unlike those of intimate partners that require a different approach. We address the societal concerns and needs of public safety, by providing youth with necessary and supportive accountability for their abuse behaviors. We honor each family’s culture, acknowledges the trauma of parenting a teen with abusive behaviors, nurturing each family’s strengths, and empower all families to identify their individual needs. We motivate individuals, families and communities with a focus on the global and basic human need for safety. We, the program designers, are recognized as subject matter experts on the topic and have presented at numerous local, state and national venues. We offer private consultative, collaborative and experienced professional services to agencies, communities and parents. Lets talk, contact us today to help your community address Child to Parent Violence (facebook, linkedin, website and twitter)

Target Market(s)

Department of Juvenile Justice, Law Enforcement, State Attorney, Probation Officers, Child Welfare Agency, Department of Child and Family, Legislators and Parents

Industry/Entity Type

Consulting

Font styles to use
Serif

Requirements
Must have
• Colorful, professional and double sided flyer with imagery similar to domestic violence but with an adolescent as the batterer towards the parent/caregiver. Description of how Mending Roots Consulting provides a evidenced promised 10 week community based program designed to reduce teen abuse and violence within the home. And consulting services such as train the trainer for the program, presentations, parent coaching and independent educational consulting services to parents.
Nice to have
• OCR for the website

```html
<!DOCTYPE html>
<html lang="en">
<head>
<meta charset="utf-8">
<title>Mending Roots Consulting Flyer</title>
<link href="https://fonts.googleapis.com/css2?family=Arimo:wght@400;700&family=Libre+Baskerville:wght@700&display=swap" rel="stylesheet">
<style>
  :root{
    --ink:#1d1d1d;
    --blue:#1d5fb4;
    --red:#c8241f;
    --panel:#f2f2f2;
    --panel-line:#9a9a9a;
    --bar:#3a3a3a;
    --bar-top:#6a6a6a;
    --photo-warm:#c9a48a;
    --photo-cool:#8fa3b8;
  }
  *{box-sizing:border-box;margin:0;padding:0}
  html,body{width:849px;height:1200px;overflow:hidden;background:#fff}
  .flyer{position:relative;width:849px;height:1200px;font-family:"Arimo",Arial,sans-serif;color:var(--ink);background:#fff}
  .hero-photo{position:absolute;right:0;top:0;width:290px;height:138px;background:linear-gradient(135deg,#d9c4b3,var(--photo-warm) 60%,#7c6a60)}
  .intro-block{position:absolute;left:34px;top:30px;width:782px;font-size:11.5px;line-height:1.3}
  .intro{width:500px}
  .intro-2{margin-top:3px}
  .brand{color:var(--blue)}
  .effect-panel{position:absolute;left:22px;top:228px;width:805px;height:684px;background:var(--panel);border:2px solid var(--panel-line);display:flex;flex-direction:column}
  .effect-title{font-family:"Libre Baskerville",Georgia,serif;color:var(--red);font-size:19px;text-align:center;line-height:1.3;margin:10px 30px 6px}
  .effect-list{list-style:none;padding:0 26px 14px 28px;flex:1;display:flex;flex-direction:column;justify-content:space-around}
  .effect-list li{position:relative;font-size:14px;line-height:1.38;padding-left:16px}
  .effect-list li::before{content:"";position:absolute;left:0;top:7px;width:6px;height:6px;background:var(--ink)}
  .photo-row{position:absolute;left:22px;top:920px;width:805px;height:128px;display:flex;gap:6px}
  .photo-row div{flex:1}
  .photo-row .wide{flex:2.2}
  .links{position:absolute;left:0;top:1054px;width:849px;text-align:center;font-size:13px;line-height:1.35}
  .links a{color:var(--blue);text-decoration:none;display:block}
  .footer-bar{position:absolute;left:0;bottom:0;width:849px;height:82px;background:var(--bar);border-top:6px solid var(--bar-top);display:flex;align-items:center;justify-content:center}
  .footer-bar span{font-family:"Libre Baskerville",Georgia,serif;color:#fff;font-size:30px}
</style>
</head>
<body>
<div class="flyer">
  <div class="hero-photo" role="img" aria-label="Photo of a distressed teenager at home"></div>

  <div class="intro-block">
    <p class="intro"><span class="brand">Mending Roots Family Program</span> provides both parents and youth the time to grow together in their understanding of abuse. Together they acquire a variety of skills and concepts that strengthen them in this challenging area of life. MRC acknowledges parents as experts in their own families. Youth face their behaviors with accountability and without minimizing, justifying or denying their disrespectful and abusive actions. Participants forge the bonds of familial respect as they face their struggles of disrespect, abuse and violence. Together, parents and youth create shared goals for improving respect and decreasing abuse.</p>
    <p class="intro-2"><span class="brand">Mending Roots Family Program</span> groups offer a respite of civility, personal growth, and encouragement during the storms of family life. MRC addresses the societal concerns and needs of public safety, provides youth with necessary and supportive accountability for their abuse, and builds competency in developmentally appropriate social and emotional skills needed by teens to replace their abusive and violent behaviors. It is true; hope and healing are possible for families that have been ravaged and devastated by teen abuse and violence.</p>
  </div>

  <section class="effect-panel">
    <h2 class="effect-title">What makes Mending Roots Family Program so effective<br>at reducing teen abuse and violence in the home?</h2>
    <ul class="effect-list">
      <li>We understand that traditional domestic violence battery intervention, models, and philosophies for adult intimate partner abuse is not developmentally appropriate for adolescents and traditional approaches result in an increase of teen abuse and violence within the home.</li>
      <li>We recognize that the relationship between a parent-child has a distinctiveness unlike those of intimate partners.</li>
      <li>We motivate attendees with a focus on the global and basic human need for safety.</li>
      <li>We provide a relationship based positive peer setting where teens are weekly accountable in a group setting for their behaviors toward parents.</li>
      <li>We emphasis on safety combined with the parent component serves as a highly protective factor for the contagion challenge typical in delinquent settings.</li>
      <li>We facilitate a safe, open, and non-judgmental environment where family units of any culture can work together as a parent child team to address the abusive behaviors that are particular to their home.</li>
      <li>We deliver lessons that target key concepts and universally recognized communication skills to address behaviors and the underlying emotions that developed into a domestic violence charge.</li>
      <li>We incorporate the Substance Abuse and Mental Health Services Administration (SAMHSA) System of Care Principles and Values.</li>
      <li>We, the program designers, are recognized as subject matter experts on the topic and have presented at numerous state and national venues.</li>
      <li>We understand the complex nuances of this form of domestic violence having served over 150 teens charged with Domestic Violence or Battery against a caregiver with a total of over 200 individuals including parents or other caregivers.</li>
    </ul>
  </section>

  <div class="photo-row">
    <div role="img" aria-label="Photo of a parent and teen talking" style="background:linear-gradient(135deg,#b8a595,var(--photo-cool))"></div>
    <div role="img" aria-label="Photo of a family group session" style="background:linear-gradient(135deg,#a7b5a0,#c7b59a)"></div>
    <div class="wide" role="img" aria-label="Photo of smiling children together" style="background:linear-gradient(135deg,#e3c7a8,#b9c9dc)"></div>
    <div role="img" aria-label="Photo of a parent hugging a teen" style="background:linear-gradient(135deg,#c2a995,#8d9fb1)"></div>
    <div role="img" aria-label="Photo of a teen and caregiver outdoors" style="background:linear-gradient(135deg,#9fb59a,#d4bfa4)"></div>
  </div>

  <div class="links">
    <a href="#">www.hearthwardsupport.example</a>
    <a href="#">https://www.socialpage.example/MRConsulting</a>
    <a href="#">https://www.shortposts.example/parent_abuse</a>
  </div>

  <footer class="footer-bar"><span>Mending Roots Consulting, Inc.</span></footer>
</div>
</body>
</html>
```